Website for Apartment Rental in Prague

I would like to create designs of my website focused on luxury apartment rentals in Prague, Czech Republic. I created initial mock-ups, They are all attached. I need to design homepage and subpage. The mock-ups were created by combining elements from different websites that I liked but I need you to create a design that is unique and original. The attached files a only a guidance for the structure of the website but not for the design. Try to be creative.

Industry/Entity Type

Apartment

```html
<!DOCTYPE html>
<html lang="en">
<head>
<meta charset="utf-8">
<title>Maison Lumen Apartments Prague</title>
<link rel="stylesheet" href="https://fonts.googleapis.com/css2?family=Questrial&family=Lato:wght@400;700;900&family=Oswald:wght@400;500&display=swap">
<style>
:root{
  --gold:#b9a16b;
  --gold-dark:#a88f58;
  --ink:#222;
  --text:#333;
  --muted:#777;
  --line:#d8d8d8;
  --topbar:#f2f2f2;
  --nav:#2e2e2e;
  --soft:#f3f3f3;
  --footer:#070707;
  --footer-base:#1e1e1e;
  --white:#fff;
}
*{box-sizing:border-box;margin:0;padding:0}
html,body{width:1200px;height:3114px;overflow:hidden}
body{font-family:'Lato',sans-serif;color:var(--text);background:var(--white);position:relative}
.abs{position:absolute}
.heading{font-family:'Questrial',sans-serif;color:var(--gold);font-size:30px;text-align:center;position:absolute;left:0;width:1200px;letter-spacing:.5px}
.heading::after{content:"";display:block;width:280px;height:1px;background:var(--line);margin:10px auto 0}

/* top bar */
.topbar{top:0;left:0;width:1200px;height:33px;background:var(--topbar);font-size:11px;color:#444}
.topbar .lang{left:141px;top:10px;display:flex;align-items:center;gap:6px}
.flag{width:14px;height:9px;background:linear-gradient(#c8102e 0 33%,#fff 33% 66%,#012169 66%)}
.topbar .hospitality{left:238px;top:10px}
.topbar .mail{left:754px;top:10px;display:flex;gap:6px;align-items:center}
.topbar .phone{left:960px;top:10px;display:flex;gap:6px;align-items:center}

/* header */
.header{top:33px;left:0;width:1200px;height:73px}
.brand{left:141px;top:12px;font-family:'Lato',sans-serif;font-weight:700;color:var(--gold);font-size:17px;letter-spacing:1px;line-height:22px}
.brand span{display:block;color:var(--ink);font-size:17px}
.search{left:868px;top:18px;width:190px;height:30px;border:1px solid var(--line);border-radius:15px;font-size:11px;color:#555;padding:8px 14px}
.search .go{position:absolute;right:2px;top:2px;width:24px;height:24px;border-radius:50%;background:#ddd}

/* nav */
.nav{top:106px;left:0;width:1200px;height:33px;background:var(--nav)}
.nav ul{list-style:none;position:absolute;left:141px;width:918px;top:0;height:33px;display:flex;justify-content:space-between;align-items:center}
.nav li{color:var(--white);font-size:11px;font-weight:700;letter-spacing:.6px;text-transform:uppercase}

/* hero */
.hero{top:139px;left:0;width:1200px;height:546px;overflow:hidden}
.hero-photo{position:absolute;inset:0;background:linear-gradient(180deg,#cfd0cc 0%,#b6b5b0 35%,#8f8d87 60%,#6c6a66 100%)}
.hero-title{position:absolute;top:372px;width:1200px;text-align:center;font-family:'Oswald',sans-serif;font-size:34px;color:var(--white);letter-spacing:-.5px}
.hero-arrow{position:absolute;top:240px;width:20px;height:30px;background:rgba(255,255,255,.85);display:flex;align-items:center;justify-content:center}
.hero-wave{position:absolute;left:0;top:366px}

/* booking */
.booking-title{top:672px}
.field{position:absolute;top:754px;height:30px;border:1px solid var(--line);font-size:11px;color:#555;padding:8px 10px;display:flex;align-items:center;gap:8px}
.select{padding:8px 6px;justify-content:space-between}
.cta{position:absolute;top:822px;left:413px;width:374px;height:32px;display:flex}
.cta div{flex:1;background:var(--gold);color:var(--white);font-size:13px;font-weight:700;display:flex;align-items:center;justify-content:center;letter-spacing:.3px}
.cta .or{position:absolute;left:175px;top:4px;width:24px;height:24px;border-radius:50%;background:var(--white);color:var(--ink);font-size:10px;font-weight:900;display:flex;align-items:center;justify-content:center}

/* vision */
.vision{top:930px;left:0;width:1200px;height:360px;background:var(--soft)}
.vision-title{top:1000px}
.vision-text{top:1078px;left:170px;width:860px;font-size:14px;font-weight:700;text-align:center;line-height:23px;color:var(--ink)}

/* listings */
.listing-title{top:1282px}
.card{position:absolute;width:287px;height:233px;overflow:hidden;box-shadow:0 10px 8px -6px rgba(0,0,0,.45)}
.card .photo{position:absolute;inset:0}
.card .band{position:absolute;left:0;bottom:0;width:100%;height:75px;background:rgba(20,20,20,.72);padding:10px 24px;color:var(--white)}
.card .price{font-size:19px;font-weight:700;margin-top:-30px;text-shadow:0 1px 2px rgba(0,0,0,.5)}
.card .desc{font-size:12px;font-weight:700;line-height:16px;margin-top:8px}
.card .home{position:absolute;right:12px;top:12px}
.card.featured .over{position:absolute;inset:0;background:rgba(25,25,25,.85);color:var(--white);padding:10px 16px}
.featured .price{font-size:23px;font-weight:700;margin:0;text-shadow:none}
.featured .addr{display:flex;gap:8px;font-size:12px;font-weight:700;margin-top:26px;line-height:16px}
.featured .blurb{font-size:11px;color:#bbb;line-height:15px;margin-top:8px}
.featured .facts{position:absolute;left:0;bottom:0;width:100%;height:60px;display:flex;border-top:1px solid #555}
.featured .facts div{flex:1;border-right:1px solid #555;display:flex;flex-direction:column;align-items:center;justify-content:center;gap:4px;font-size:8px}
.list-arrow{position:absolute;top:1600px}

/* testimonials */
.testimonials{top:1969px;left:0;width:1200px;height:482px;overflow:hidden}
.testimonials .photo{position:absolute;inset:0;background:radial-gradient(ellipse at 55% 55%,#4a4238 0%,#2a2721 45%,#141414 100%)}
.testimonials .shade{position:absolute;inset:0;background:rgba(0,0,0,.45)}
.testimonial-title{top:2040px;color:var(--gold)}
.testimonial-title::after{background:#777}
.portrait{top:2125px;left:145px;width:240px;height:166px;border:4px solid var(--white);background:linear-gradient(160deg,#6d8a4c 0%,#a39373 55%,#5a5a3e 100%)}
.quote-box{top:2185px;left:359px;width:48px;height:48px;background:var(--gold);display:flex;align-items:center;justify-content:center}
.testimonial-text{top:2143px;left:436px;width:616px;color:#eee;font-size:13px;line-height:19.5px}
.testimonial-name{top:2255px;left:436px;color:var(--white);font-size:12px;font-weight:700;letter-spacing:.5px}
.dots{top:2281px;left:436px;display:flex;gap:5px}
.dots span{width:6px;height:6px;border-radius:50%;background:#aaa}
.dots span:first-child{background:var(--white)}
.testimonial-wave{position:absolute;left:0;bottom:0}

/* newsletter */
.news-title{top:2456px}
.input{position:absolute;top:2538px;height:34px;border:1px solid var(--line);font-size:11px;color:#666;padding:10px 10px}
.subscribe{top:2609px;left:519px;width:162px;height:33px;background:var(--gold);color:var(--white);font-size:14px;font-weight:700;display:flex;align-items:center;justify-content:center}

/* footer */
.footer{top:2715px;left:0;width:1200px;height:359px;background:var(--footer);color:#ddd}
.footer h4{position:absolute;top:60px;font-size:14px;font-weight:700;color:var(--white);padding-bottom:10px;border-bottom:1px solid #333}
.quick{position:absolute;left:141px;top:107px;list-style:none;font-size:11px;line-height:26.6px}
.quick li::before{content:"›";margin-right:10px;color:#aaa}
.know{position:absolute;left:355px;top:112px;width:270px}
.know .item{display:flex;gap:16px;margin-bottom:16px;font-size:10.5px;line-height:15px}
.know .item b{color:var(--gold);font-weight:700;font-size:11px;display:block}
.ring{width:26px;height:26px;border-radius:50%;border:1px solid #777;flex:none;display:flex;align-items:center;justify-content:center}
.contact{position:absolute;left:690px;top:108px;width:210px;font-size:10.5px;line-height:15px}
.contact .row{display:flex;gap:14px;margin-bottom:26px}
.contact b{color:var(--white)}
.follow{position:absolute;left:947px;top:110px;font-size:11px}
.follow .row{display:flex;align-items:center;gap:10px;margin-bottom:16px}
.follow i{width:24px;height:24px;border-radius:50%;display:block}
.copyright{top:3074px;left:0;width:1200px;height:40px;background:var(--footer-base);color:#bbb;font-size:11px;display:flex;align-items:center;justify-content:center}
</style>
</head>
<body>

<div class="abs topbar">
  <div class="abs lang"><span class="flag"></span>English <span style="font-size:8px">▼</span></div>
  <div class="abs hospitality">Our Hospitality</div>
  <div class="abs mail">
    <svg width="13" height="9" viewBox="0 0 13 9"><rect x=".5" y=".5" width="12" height="8" fill="none" stroke="#555"/><path d="M.5 .5 6.5 5 12.5 .5" fill="none" stroke="#555"/></svg>
    reservations@lumenstays.com
  </div>
  <div class="abs phone">
    <svg width="10" height="11" viewBox="0 0 10 11"><path d="M2 0 4 3 3 4.5C4 6.5 5 7.5 6.5 8L8 7 10 9 8.5 11C4 10 1 7 0 2Z" fill="#555"/></svg>
    +420 601 482 315
  </div>
</div>

<header class="abs header">
  <div class="abs brand">MAISON LUMEN APARTMENTS<span>PRAGUE</span></div>
  <div class="abs search">Discover Prague<span class="go"></span></div>
</header>

<nav class="abs nav">
  <ul>
    <li>Apartments</li><li>Location</li><li>Services</li><li>Gallery</li><li>News</li><li>Exclusive Offers &amp; Tours</li><li>For Families</li><li>Contact Us</li>
  </ul>
</nav>

<section class="abs hero">
  <div class="hero-photo" role="img" aria-label="Bright luxury apartment living room with grey sofas, a round coffee table and a dining area by tall windows"></div>
  <div class="hero-title">BEING HOME IN PRAGUE</div>
  <div class="hero-arrow" style="left:0"><svg width="8" height="12" viewBox="0 0 8 12"><path d="M7 1 2 6 7 11" fill="none" stroke="#333" stroke-width="2"/></svg></div>
  <div class="hero-arrow" style="right:0"><svg width="8" height="12" viewBox="0 0 8 12"><path d="M1 1 6 6 1 11" fill="none" stroke="#333" stroke-width="2"/></svg></div>
  <svg class="hero-wave" width="1200" height="180" viewBox="0 0 1200 180">
    <path d="M0 164 Q300 128 600 90 Q900 128 1200 164" fill="none" stroke="#b9a16b" stroke-width="3"/>
    <path d="M0 172 Q300 136 600 97 Q900 136 1200 172 L1200 180 L0 180Z" fill="#fff"/>
  </svg>
</section>

<h2 class="heading booking-title">Official Site - Best Price Guaranteed</h2>
<div class="field" style="left:141px;width:216px">
  <svg width="11" height="11" viewBox="0 0 11 11"><rect x=".5" y="1.5" width="10" height="9" fill="none" stroke="#555"/><path d="M.5 4h10" stroke="#555"/></svg>Check In Date</div>
<div class="field" style="left:376px;width:214px">
  <svg width="11" height="11" viewBox="0 0 11 11"><rect x=".5" y="1.5" width="10" height="9" fill="none" stroke="#555"/><path d="M.5 4h10" stroke="#555"/></svg>Check Out Date</div>
<div class="field select" style="left:614px;width:56px">Adults <span style="font-size:7px">▼</span></div>
<div class="field select" style="left:680px;width:78px">Children <span style="font-size:7px">▼</span></div>
<div class="field select" style="left:764px;width:62px">Infants <span style="font-size:7px">▼</span></div>
<div class="field" style="left:841px;width:217px">Promotional Code</div>
<div class="cta">
  <div>CHECK AVAILABILITY</div>
  <div>SELECT RENTAL UNIT &nbsp;&nbsp;&nbsp;<span style="font-size:8px">▼</span></div>
  <span class="or">OR</span>
</div>

<section class="abs vision">
  <svg style="position:absolute;left:0;bottom:0" width="1200" height="80" viewBox="0 0 1200 80">
    <path d="M0 78 L600 8 L1200 78 L1200 80 L0 80Z" fill="#fff"/>
    <path d="M0 76 L600 6 L1200 76" fill="none" stroke="#e2e2e2" stroke-width="2"/>
  </svg>
</section>
<h2 class="heading vision-title">A Different Vision Of Travelling</h2>
<p class="abs vision-text">Something spectacular has arrived in the heart of Europe. Steps from Old Town, this rental experience is curated with world-class amenities, exemplary style and a level of convenience you have to experience to believe. Experience the different vision of luxury in center of Prague.</p>

<h2 class="heading listing-title">Featured Listing</h2>

<svg class="list-arrow" style="left:84px" width="20" height="38" viewBox="0 0 20 38"><path d="M18 1 2 19 18 37" fill="none" stroke="#444" stroke-width="2"/></svg>
<svg class="list-arrow" style="left:1096px" width="20" height="38" viewBox="0 0 20 38"><path d="M2 1 18 19 2 37" fill="none" stroke="#444" stroke-width="2"/></svg>

<article class="card featured" style="left:141px;top:1360px">
  <div class="photo" role="img" aria-label="Apartment interior photo" style="background:linear-gradient(135deg,#8a8075,#4a443e)"></div>
  <div class="over">
    <div class="price">$689,000</div>
    <svg class="home" width="16" height="14" viewBox="0 0 16 14"><path d="M8 0 16 7H14V14H10V9H6V14H2V7H0Z" fill="#fff"/></svg>
    <div class="addr"><svg width="10" height="14" viewBox="0 0 10 14"><path d="M5 0C2 0 0 2 0 5 0 8 5 14 5 14S10 8 10 5C10 2 8 0 5 0ZM5 7A2 2 0 1 1 5 3 2 2 0 0 1 5 7Z" fill="#fff"/></svg><span>12 - Karlova Lane, Old Town,<br>Prague - 11000</span></div>
    <div class="blurb">Lorem ipsum dolor sit amet, consectetuer adipisci elit, sed diam nonummy nibh euismod tinc</div>
    <div class="facts">
      <div><svg width="18" height="18" viewBox="0 0 18 18"><rect x="1" y="1" width="16" height="16" fill="none" stroke="#fff" stroke-width="1.5"/><path d="M1 1 17 17M17 1 1 17" stroke="#fff"/></svg>3,000 S/F</div>
      <div><svg width="22" height="16" viewBox="0 0 22 16"><path d="M1 2V15M1 10H21V15M4 7H10V10" fill="none" stroke="#fff" stroke-width="2"/></svg>4 Bedrooms</div>
      <div><svg width="20" height="16" viewBox="0 0 20 16"><path d="M1 8H19V11C19 13 17 15 15 15H5C3 15 1 13 1 11ZM3 8V2H7" fill="none" stroke="#fff" stroke-width="2"/></svg>4 Baths</div>
      <div style="border-right:0"><svg width="22" height="18" viewBox="0 0 22 18"><path d="M1 8 11 1 21 8M5 17V12H17V17" fill="none" stroke="#fff" stroke-width="2"/></svg>2 Garages</div>
    </div>
  </div>
</article>

<article class="card" style="left:457px;top:1360px">
  <div class="photo" role="img" aria-label="Living room with a tan leather sofa and tall windows" style="background:linear-gradient(160deg,#d9d2c6,#8a6a4d)"></div>
  <svg class="home" width="16" height="14" viewBox="0 0 16 14"><path d="M8 0 16 7H14V14H10V9H6V14H2V7H0Z" fill="#222"/></svg>
  <div class="band"><div class="price">$500,00</div><div class="desc">Lorem ipsum dolor sit amet,<br>consectetuer adipiscin diam nonu</div></div>
</article>

<article class="card" style="left:773px;top:1360px">
  <div class="photo" role="img" aria-label="Bright lounge with a grey sofa and wall art" style="background:linear-gradient(160deg,#e6e2da,#9c8d7a)"></div>
  <svg class="home" width="16" height="14" viewBox="0 0 16 14"><path d="M8 0 16 7H14V14H10V9H6V14H2V7H0Z" fill="#222"/></svg>
  <div class="band"><div class="price">$354,000</div><div class="desc">Lorem ipsum dolor sit amet,<br>consectetuer adipiscin diam nonu</div></div>
</article>

<article class="card" style="left:141px;top:1651px">
  <div class="photo" role="img" aria-label="Cream bedroom with bedside lamp and decor" style="background:linear-gradient(160deg,#ece4d3,#a89478)"></div>
  <svg class="home" width="16" height="14" viewBox="0 0 16 14"><path d="M8 0 16 7H14V14H10V9H6V14H2V7H0Z" fill="#222"/></svg>
  <div class="band"><div class="price">$250,00</div><div class="desc">Lorem ipsum dolor sit amet,<br>consectetuer adipiscin diam nonu</div></div>
</article>

<article class="card" style="left:457px;top:1651px">
  <div class="photo" role="img" aria-label="Bedroom with grey bedding and warm lamp light" style="background:linear-gradient(160deg,#b8a48c,#5a4a3c)"></div>
  <svg class="home" width="16" height="14" viewBox="0 0 16 14"><path d="M8 0 16 7H14V14H10V9H6V14H2V7H0Z" fill="#222"/></svg>
  <div class="band"><div class="price">$210,00</div><div class="desc">Lorem ipsum dolor sit amet,<br>consectetuer adipiscin diam nonu</div></div>
</article>

<article class="card" style="left:773px;top:1651px">
  <div class="photo" role="img" aria-label="Bedroom with white bed and tall curtained windows" style="background:linear-gradient(160deg,#e9e1d0,#8d7a62)"></div>
  <svg class="home" width="16" height="14" viewBox="0 0 16 14"><path d="M8 0 16 7H14V14H10V9H6V14H2V7H0Z" fill="#222"/></svg>
  <div class="band"><div class="price">$750,000</div><div class="desc">Lorem ipsum dolor sit amet,<br>consectetuer adipiscin diam nonu</div></div>
</article>

<section class="abs testimonials">
  <div class="photo" role="img" aria-label="Family relaxing on a lawn in front of a house, dimmed as background"></div>
  <div class="shade"></div>
  <svg class="testimonial-wave" width="1200" height="90" viewBox="0 0 1200 90">
    <path d="M0 82 Q300 40 600 6 Q900 40 1200 82 L1200 90 L0 90Z" fill="#fff"/>
    <path d="M0 80 Q300 38 600 3 Q900 38 1200 80" fill="none" stroke="#ddd" stroke-width="2"/>
  </svg>
</section>
<h2 class="heading testimonial-title">Client Testimonials</h2>
<div class="abs portrait" role="img" aria-label="Portrait of a happy family sitting on grass"></div>
<div class="abs quote-box"><svg width="22" height="18" viewBox="0 0 22 18"><path d="M0 18V9C0 4 3 1 8 0V3C5 4 4 6 4 8H9V18ZM12 18V9C12 4 15 1 20 0V3C17 4 16 6 16 8H21V18Z" fill="#fff"/></svg></div>
<p class="abs testimonial-text">Maison Lumen apartments offers short term and as well as long term options in our studio apartments and our one bedroom apartment homes. Our luxurious apartments and high quality customer service have allowed us to dominate the Prague apartment market with a proven track record. Our years of experience and knowledge have made us a premier apartment rental company as we continue to stress the importance of servicing individuals and corporations who are seeking the finest accommodations.</p>
<div class="abs testimonial-name">DANIEL HART</div>
<div class="abs dots"><span></span><span></span><span></span><span></span></div>

<h2 class="heading news-title">Newsletter Signup</h2>
<div class="input" style="left:187px;width:401px">Enter your name</div>
<div class="input" style="left:613px;width:400px">Enter your email</div>
<div class="abs subscribe">SUBSCRIBE NOW!</div>

<footer class="abs footer">
  <h4 style="left:141px;width:180px">Quick Links</h4>
  <h4 style="left:355px;width:280px">Need To Know</h4>
  <h4 style="left:690px;width:200px">Contact Details</h4>
  <h4 style="left:947px;width:110px">Follow Us</h4>

  <ul class="quick">
    <li>Apartments</li><li>Location</li><li>Services</li><li>Gallery</li><li>News</li><li>Exclusive Offers &amp; Tours</li><li>For Families</li><li>Contact Us</li>
  </ul>

  <div class="know">
    <div class="item"><span class="ring"><svg width="10" height="12" viewBox="0 0 10 12"><rect x="1" y="1" width="8" height="10" fill="none" stroke="#ccc"/><path d="M3 4H7M3 7H7" stroke="#ccc"/></svg></span><div><b>Apartments</b>Also Available To Rent All The Apartments Together For Companies Or Larger Groups.</div></div>
    <div class="item" style="margin-top:10px"><span class="ring"><svg width="12" height="12" viewBox="0 0 12 12"><circle cx="6" cy="6" r="5" fill="none" stroke="#ccc"/><path d="M6 3V6H8" fill="none" stroke="#ccc"/></svg></span><div><b>Check-out</b>12 Noon; Earliest Check-in, 3pm - Both Are Flexible, By Arrangement.</div></div>
    <div class="item"><span class="ring"><svg width="12" height="12" viewBox="0 0 12 12"><path d="M1 6 6 1H11V6L6 11Z" fill="none" stroke="#ccc"/></svg></span><div><b>Rates</b>Prices From 150 USD Per Night, Including Tax</div></div>
  </div>

  <div class="contact">
    <div class="row"><svg width="10" height="14" viewBox="0 0 10 14"><path d="M5 0C2 0 0 2 0 5 0 8 5 14 5 14S10 8 10 5C10 2 8 0 5 0ZM5 7A2 2 0 1 1 5 3 2 2 0 0 1 5 7Z" fill="#ccc"/></svg><div><b>MAISON LUMEN APARTMENTS PRAGUE</b><br>1234 Lorem Ipsum Dolor,<br>Mie Zuwert, CA. 1234</div></div>
    <div class="row"><svg width="11" height="12" viewBox="0 0 10 11"><path d="M2 0 4 3 3 4.5C4 6.5 5 7.5 6.5 8L8 7 10 9 8.5 11C4 10 1 7 0 2Z" fill="#ccc"/></svg><div>+420 601 482 315</div></div>
    <div class="row"><svg width="12" height="12" viewBox="0 0 12 12"><rect x="1" y="4" width="10" height="6" fill="none" stroke="#ccc"/><rect x="3" y="1" width="6" height="3" fill="none" stroke="#ccc"/></svg><div>+420 601 482 315</div></div>
    <div class="row"><svg width="13" height="9" viewBox="0 0 13 9"><rect x=".5" y=".5" width="12" height="8" fill="none" stroke="#ccc"/><path d="M.5 .5 6.5 5 12.5 .5" fill="none" stroke="#ccc"/></svg><div>reservations@lumenstays.com</div></div>
  </div>

  <div class="follow">
    <div class="row"><i style="background:#3b5a98"></i>Friendbook</div>
    <div class="row"><i style="background:#2aa3e0"></i>Chirper</div>
    <div class="row"><i style="background:#1b78b4"></i>WorkLink</div>
    <div class="row"><i style="background:#d34836"></i>Circles</div>
  </div>
</footer>
<div class="abs copyright">Copyright © 2017 Maison Lumen Apartments Prague. All Right Reserved.</div>

</body>
</html>
```